Web Design Project - KornHaus.de

The page shall provide individual brown-bread mix.
There shall be presented:
* RECIPES: consumer's choice and feedback area
* EQUIPMENT: baking equipment store
* BREAD-MIX: individual mix and configurator function for bread-mix
The consumer can search/view the content and checkout the products. A user can establish a profile. A user can interact on the page for feedback on content and connection to social media.

```html
<!DOCTYPE html>
<html lang="en">
<head>
<meta charset="utf-8">
<title>KornHaus.de</title>
<link href="https://fonts.googleapis.com/css2?family=Ubuntu:wght@400;500;700&family=Arimo:wght@400;700&family=Cormorant+Garamond:ital,wght@1,400&display=swap" rel="stylesheet">
<style>
:root{
  --topbar:#5a1505;
  --nav:#5e1a0a;
  --footer:#5b1608;
  --cream:#fbeec8;
  --cream-deep:#f6e0a8;
  --page:#fdf3de;
  --red:#c8323a;
  --darkred:#7a1a0c;
  --gold:#d9a818;
  --navgold:#f2b51c;
  --text:#3a2a22;
  --grey:#e4e4e4;
  --white:#ffffff;
  --btn:#5a1505;
}
*{box-sizing:border-box;margin:0;padding:0}
html,body{width:875px;height:1200px;overflow:hidden}
body{position:relative;background:var(--page);font-family:'Arimo',Arial,sans-serif;color:var(--text)}
.abs{position:absolute}
.topbar{left:0;top:0;width:875px;height:37px;background:var(--topbar)}
.currency-label{left:39px;top:11px;font-size:12px;color:var(--navgold)}
.currency-select{left:90px;top:9px;width:61px;height:18px;background:#2e0a03;color:#fff;font-size:11px;padding:3px 0 0 7px}
.currency-select svg{position:absolute;right:4px;top:6px}
.social{top:5px;width:26px;height:26px;background:var(--navgold);border:1px solid #f7d77a}
.header{left:0;top:37px;width:875px;height:101px;background:linear-gradient(90deg,var(--cream) 0%,var(--cream-deep) 60%,var(--cream) 100%)}
.logo{left:22px;top:42px;font-family:'Ubuntu',sans-serif;font-weight:500;font-size:58px;color:var(--red);letter-spacing:-1px}
.search-field{left:436px;top:103px;width:186px;height:24px;background:#f3e8a0;font-size:11px;color:#b8a878;text-align:center;line-height:24px}
.account{left:632px;top:45px;width:243px;height:67px;background:linear-gradient(#fff,#ebebeb)}
.cart-icon{left:637px;top:52px}
.acc-title{left:697px;top:69px;font-size:12px;color:var(--red)}
.acc-sub{left:697px;top:83px;font-size:12px;color:#222}
.acc-count{left:796px;top:63px;font-size:30px;font-weight:700;color:#222}
.acc-items{left:823px;top:83px;font-size:12px;color:#222}
.welcome-strip{left:640px;top:112px;width:235px;height:25px;background:var(--red);color:#fff;font-size:11px;line-height:25px;padding-left:9px}
.nav{left:0;top:138px;width:875px;height:47px;background:var(--nav)}
.nav a{position:absolute;top:15px;font-size:13.5px;font-weight:700;color:#fff;text-decoration:none}
.nav a.active{color:var(--navgold)}
.hero{left:20px;top:192px;width:835px;height:338px;background:
  radial-gradient(ellipse 35% 45% at 22% 18%,rgba(214,178,110,.75),transparent 70%),
  radial-gradient(ellipse 30% 35% at 68% 20%,rgba(214,140,70,.85),transparent 70%),
  radial-gradient(ellipse 25% 35% at 84% 45%,rgba(196,120,58,.85),transparent 70%),
  radial-gradient(ellipse 35% 35% at 55% 70%,rgba(226,176,120,.8),transparent 70%),
  linear-gradient(135deg,#b88850,#8e5224 55%,#5e3014)}
.hero-price{left:22px;top:388px;color:#fff;font-family:'Cormorant Garamond',serif;font-style:italic;font-size:42px}
.hero-price sup{font-size:28px}
.hero-title{left:44px;top:442px;font-family:'Arimo',sans-serif;font-weight:700;font-size:30px;color:#fff}
.hero-text{left:57px;top:486px;width:310px;font-size:10.5px;line-height:15px;color:#fff}
h2{font-family:'Ubuntu',sans-serif;font-weight:500;color:var(--red)}
.welcome-h{left:27px;top:546px;font-size:22px}
.welcome-p{left:27px;top:580px;width:592px;font-size:10.6px;line-height:17px;color:#333}
.recipes{left:16px;top:678px;width:598px;height:375px;background:#f4f4f4;border:2px solid #d6d6d6}
.recipes-inner{left:22px;top:684px;width:586px;height:363px;background:#fff}
.recipes-h{left:36px;top:685px;font-size:23px}
.strip{left:22px;top:718px;width:586px;height:70px;background:var(--grey)}
.thumb{top:727px;width:76px;height:52px;border:2px solid #fff;background:linear-gradient(135deg,#c07a3e,#8a4a1e)}
.recipe-img{left:27px;top:797px;width:162px;height:135px;background:linear-gradient(135deg,#d8c7a0,#b9773c 55%,#7a4a22)}
.ing-h{left:40px;top:941px;font-size:11px;font-weight:700;color:var(--darkred)}
.ing{left:40px;top:958px;font-size:11px;color:#222;border-collapse:collapse}
.ing td{padding:0;height:20px;line-height:20px}
.recipe-title{left:209px;top:798px;font-family:'Arimo',sans-serif;font-weight:700;font-size:18px;color:var(--darkred)}
.recipe-text{left:209px;top:827px;width:392px;font-size:10.4px;line-height:16px;color:#222}
.recipe-text p{margin-bottom:16px}
.enjoy{color:var(--darkred);font-size:12px}
.choice-h{left:633px;top:556px;font-size:22px}
.product{left:630px;width:220px;height:117px;border-bottom:1px solid #e0cfae}
.product .pimg{position:absolute;left:3px;top:0;width:110px;height:68px;border:3px solid #fff;background:linear-gradient(135deg,#d1954e,#9a5422)}
.product .pname{position:absolute;left:124px;top:2px;font-size:12.5px;font-weight:700;color:var(--darkred)}
.product .qty{position:absolute;left:126px;top:23px;font-size:10.5px;color:#222}
.product .buy{position:absolute;left:126px;top:44px;width:47px;height:20px;background:var(--btn);color:#fff;font-size:11px;text-align:center;line-height:20px}
.product .pdesc{position:absolute;left:16px;top:73px;width:200px;font-size:10.5px;line-height:15px;color:#222}
.footer{left:0;top:1070px;width:875px;height:130px;background:var(--footer)}
.fb-h{left:30px;top:1081px;font-size:13px;font-weight:700;color:var(--navgold)}
.f-label{font-size:10.5px;color:#fff}
.f-input{background:#9a5550;border:1px solid #b27068}
.f-btn{top:1175px;height:14px;background:var(--red);color:#fff;font-size:10.5px;text-align:center;line-height:14px}
.pay-label{left:663px;top:1088px;font-size:11px;color:#fff}
.card{top:1086px;width:27px;height:18px;background:#f2f2f2;border-radius:2px}
.f-links{right:29px;top:1130px;font-size:11px;color:#fff}
.copyright{right:33px;top:1166px;font-size:11px;color:#fff}
</style>
</head>
<body>

<div class="abs topbar"></div>
<div class="abs currency-label">Currency</div>
<div class="abs currency-select">Doller<svg width="8" height="5"><path d="M0 0L4 5L8 0Z" fill="#c8323a"/></svg></div>
<div class="abs social" style="left:767px" role="img" aria-label="Social network link"></div>
<div class="abs social" style="left:797px" role="img" aria-label="Social network link"></div>
<div class="abs social" style="left:827px" role="img" aria-label="News feed link"></div>

<div class="abs header"></div>
<div class="abs logo">KornHaus</div>
<svg class="abs" style="left:395px;top:40px" width="250" height="98">
  <polygon points="38,52 250,52 250,98 0,98" fill="#d9a818"/>
  <circle cx="193" cy="31" r="10" fill="none" stroke="#5a1505" stroke-width="4"/>
  <line x1="200" y1="38" x2="214" y2="54" stroke="#5a1505" stroke-width="5" stroke-linecap="round"/>
</svg>
<div class="abs search-field">Enter search keyword here</div>
<div class="abs account"></div>
<svg class="abs cart-icon" width="56" height="56">
  <path d="M4 6H12L18 34H46L52 12H14" fill="none" stroke="#666" stroke-width="3"/>
  <rect x="16" y="14" width="34" height="18" fill="#9a9a9a"/>
  <circle cx="22" cy="44" r="4" fill="#444"/><circle cx="42" cy="44" r="4" fill="#444"/>
</svg>
<div class="abs acc-title">Your Account</div>
<div class="abs acc-sub">Now in your cart</div>
<div class="abs acc-count">0</div>
<div class="abs acc-items">items</div>
<div class="abs welcome-strip">Welcome , ( Log in )</div>

<nav class="abs nav">
  <a class="active" style="left:164px">Home</a>
  <a style="left:236px">About Us</a>
  <a style="left:331px">Bread Mix</a>
  <a style="left:430px">Recipes</a>
  <a style="left:517px">Consumer choice</a>
  <a style="left:663px">Contact Us</a>
</nav>

<div class="abs hero" role="img" aria-label="Photo of assorted seeded bread loaves on burlap with wheat ears"></div>
<svg class="abs" style="left:0;top:360px" width="875" height="175">
  <polygon points="8,7 545,170 20,170" fill="#c8323a"/>
  <polygon points="780,170 858,130 858,170" fill="#4a1206"/>
  <path d="M824 150L819 156L824 162" fill="none" stroke="#e6c07a" stroke-width="2"/>
  <path d="M841 150L846 156L841 162" fill="none" stroke="#f2b51c" stroke-width="2"/>
</svg>
<div class="abs hero-price"><sup>$</sup>28.99</div>
<div class="abs hero-title">Lorem Ipsum</div>
<div class="abs hero-text">Lorem ipsum dolor sit amet, consectetur adipisicing elit, sed do eiusmod tempor incididunt ut labore et dolore magna aliqua.</div>

<h2 class="abs welcome-h">Welcome to our site</h2>
<p class="abs welcome-p">At vero eos et accusamus et iusto odio dignissimos ducimus qui blanditiis praesentium voluptatum deleniti atque corrupti quos dolores et quas molestias excepturi sint occaecati cupiditate non provident, similique sunt in culpa qui officia deserunt mollitia animi, id est laborum et dolorum fuga. Et harum quidem rerum facilis est et expedita distinctio. Nam libero tempore, cum soluta nobis est eligendi optio cumque nihil impedit quo minus id quod maxime placeat facere possimus.</p>

<div class="abs recipes"></div>
<div class="abs recipes-inner"></div>
<h2 class="abs recipes-h">Todays Recipes</h2>
<div class="abs strip"></div>
<svg class="abs" style="left:22px;top:742px" width="586" height="22">
  <path d="M10 3L4 11L10 19Z" fill="#5a1505"/>
  <path d="M573 3L579 11L573 19Z" fill="#5a1505"/>
</svg>
<div class="abs thumb" style="left:40px" role="img" aria-label="Sliced brown bread"></div>
<div class="abs thumb" style="left:133px" role="img" aria-label="Sliced bread on a plate"></div>
<div class="abs thumb" style="left:226px" role="img" aria-label="Sliced brown bread"></div>
<div class="abs thumb" style="left:321px" role="img" aria-label="Sliced brown bread"></div>
<div class="abs thumb" style="left:414px" role="img" aria-label="Sliced bread on a plate"></div>
<div class="abs thumb" style="left:507px" role="img" aria-label="Sliced brown bread"></div>

<div class="abs recipe-img" role="img" aria-label="Photo of sliced brown bread on a plate"></div>
<div class="abs ing-h">Ingredients</div>
<table class="abs ing">
  <tr><td style="width:63px">Flour</td><td style="width:35px">:</td><td>500 kg</td></tr>
  <tr><td>Water</td><td>:</td><td>500 ltr</td></tr>
  <tr><td>Salt</td><td>:</td><td>50 gm</td></tr>
  <tr><td>Yeast</td><td>:</td><td>&nbsp;10 gm</td></tr>
</table>
<h3 class="abs recipe-title">Brown Bread</h3>
<div class="abs recipe-text">
  <p>At vero eos et accusamus et iusto odio dignissimos ducimus qui blanditiis praesentium voluptatum deleniti atque corrupti quos dolores et quas molestias excepturi sint occaecati cupiditate non provident, similique sunt in culpa qui officia deserunt mollitia animi, id est laborum et dolorum fuga.</p>
  <p>Et harum quidem rerum facilis est et expedita distinctio. Nam libero tempore, cum soluta nobis est eligendi optio cumque nihil impedit quo minus id quod maxime placeat facere possimus, omnis voluptas assumenda est, omnis dolor repellendus.</p>
  <p>At vero eos et accusamus et iusto odio dignissimos ducimus qui blanditiis praesentium voluptatum deleniti atque corrupti quos .</p>
  <div class="enjoy">Enjoy!</div>
</div>

<h2 class="abs choice-h">Customer Choice</h2>
<svg class="abs" style="left:830px;top:558px" width="22" height="26">
  <path d="M2 10L11 2L20 10" fill="none" stroke="#c8323a" stroke-width="2"/>
  <path d="M2 16L11 24L20 16" fill="none" stroke="#5a1505" stroke-width="2"/>
</svg>

<div class="abs product" style="top:597px">
  <div class="pimg" role="img" aria-label="Sliced brown bread loaf"></div>
  <div class="pname">Product Name</div><div class="qty">Quantity : 500 gm</div><div class="buy">Buy</div>
  <div class="pdesc">At vero eos et accusamus et iusto odio dignissimos ducimus qui blanditiis.</div>
</div>
<div class="abs product" style="top:716px">
  <div class="pimg" role="img" aria-label="Sliced brown bread loaf"></div>
  <div class="pname">Product Name</div><div class="qty">Quantity : 500 gm</div><div class="buy">Buy</div>
  <div class="pdesc">At vero eos et accusamus et iusto odio dignissimos ducimus qui blanditiis.</div>
</div>
<div class="abs product" style="top:833px">
  <div class="pimg" role="img" aria-label="Sliced brown bread loaf"></div>
  <div class="pname">Product Name</div><div class="qty">Quantity : 500 gm</div><div class="buy">Buy</div>
  <div class="pdesc">At vero eos et accusamus et iusto odio dignissimos ducimus qui blanditiis.</div>
</div>
<div class="abs product" style="top:948px;border-bottom:none">
  <div class="pimg" role="img" aria-label="Sliced brown bread loaf"></div>
  <div class="pname">Product Name</div><div class="qty">Quantity : 500 gm</div><div class="buy">Buy</div>
  <div class="pdesc">At vero eos et accusamus et iusto odio dignissimos ducimus qui blanditiis.</div>
</div>

<footer class="abs footer"></footer>
<svg class="abs" style="left:0;top:1070px" width="875" height="130">
  <polygon points="0,0 280,0 420,130 0,130" fill="#6b1c0c"/>
</svg>
<div class="abs fb-h">Feed back</div>
<div class="abs f-label" style="left:27px;top:1106px">Name :</div>
<div class="abs f-input" style="left:28px;top:1121px;width:112px;height:14px"></div>
<div class="abs f-label" style="left:27px;top:1141px">Email :</div>
<div class="abs f-input" style="left:28px;top:1156px;width:112px;height:14px"></div>
<div class="abs f-label" style="left:149px;top:1106px">Suggestions :</div>
<div class="abs f-input" style="left:150px;top:1121px;width:126px;height:50px"></div>
<div class="abs f-btn" style="left:200px;width:36px">send</div>
<div class="abs f-btn" style="left:239px;width:37px">clear</div>

<div class="abs pay-label">Pay through</div>
<div class="abs card" style="left:727px" role="img" aria-label="Payment method"></div>
<div class="abs card" style="left:757px" role="img" aria-label="Payment method"></div>
<div class="abs card" style="left:787px" role="img" aria-label="Payment method"></div>
<div class="abs card" style="left:817px" role="img" aria-label="Payment method"></div>
<div class="abs f-links">Home | About Us | Bread Mix | Recipes | Consumer choice | Contact Us</div>
<div class="abs copyright">Copyright © 2011 KornHaus. All Rights Reserved</div>

</body>
</html>
```